"tide-LOOP." SoCal's Fishing Industry's single stop for the latest products, content, and services

Hi, looking for a website design for new LA based company called "tide-LOOP." Where we showcase all the latest and greatest products, services, and content in a highly visually appealing platform for all fishing manufacturers and service providers as they relate to the fishing community (manufactures and service providers pay for cost-tiered content exposure and marketing, free exposure for manufacturers and service providers will have affiliate marketing link at minimal content exposure). As well, looking to include an in-site blog, store-products, and media content such as articles, video edits, and fishing condition picture galleries. Visually, looking for a minimalist/clean/blocked/ filterable and visually captivating gallery. Looking for a color pallet with white-background, deep blue- primary, light gray- secondary, light sky blue- third. Style- cleanliness and structure of wirestack.example meets content like mkharborline.example.

Target Market(s)

Primary- Southern California/Southwest Fishing Community, Secondary- All other US Fishing Communities

Coding

Coded - Design and coding required

Number of Pages Required

5+ page

Font styles to use
Sans Serif

Colors
959595
86cfc6
cadf82
333333
0555a3

Requirements
Must have
• Fast loading, mobile friendly, Analytics page, email sign up link for emailed newsletter (that is not a full page pop-up but integrated into browse bar), integrated social media links, search bar, filter link, home page return link, minimalist and clean design. Formatted to product showcase website style- please see attached files for ideas for design format and word-logo.
Should not have
• No Clutter, No background advertisements, No long text scripts outside of products main page,

```html
<!DOCTYPE html>
<html lang="en">
<head>
<meta charset="utf-8">
<title>tide-LOOP. — Home</title>
<link rel="stylesheet" href="https://fonts.googleapis.com/css2?family=Montserrat:wght@400;500;600;700&display=swap">
<style>
  :root{
    --blue:#0555a3;
    --ink:#333333;
    --gray:#959595;
    --light:#eef0f2;
    --white:#ffffff;
    --sky:#86cfc6;
  }
  *{box-sizing:border-box;margin:0;padding:0}
  html,body{width:1200px;height:626px;overflow:hidden;background:var(--white)}
  body{font-family:"Montserrat",sans-serif;color:var(--ink);position:relative}
  .site-header{position:absolute;left:0;top:0;width:1200px;height:100px}
  .brand{position:absolute;left:60px;top:34px;font-size:26px;font-weight:500;color:var(--ink);letter-spacing:.5px}
  .utility{position:absolute;right:40px;top:22px;display:flex;align-items:center;gap:16px;font-size:10px}
  .search{width:170px;border-bottom:1px solid var(--gray);color:var(--gray);padding:2px 0 4px;font-size:10px}
  .filter-btn{background:var(--blue);color:var(--white);border-radius:12px;padding:5px 14px;font-weight:600;font-size:10px}
  .social{display:flex;gap:4px}
  .social span{width:12px;height:12px;background:var(--ink);border-radius:2px;display:block}
  .account{color:var(--ink);letter-spacing:.5px}
  .account i{font-style:normal;color:var(--gray);margin:0 10px}
  .main-nav{position:absolute;right:40px;top:60px;display:flex;gap:20px;font-size:11px;font-weight:500;letter-spacing:.3px;align-items:center}
  .main-nav .active{background:var(--blue);color:var(--white);border-radius:12px;padding:4px 12px}
  .hero{position:absolute;left:60px;top:100px;width:1080px;height:370px;background:linear-gradient(120deg,#c9cdd0 0%,#a9b0b4 35%,#5f7f9a 70%,#7fa8c4 100%)}
  .hero-title{position:absolute;left:90px;top:250px;font-size:34px;font-weight:500;line-height:1;color:#1f2427;letter-spacing:.5px}
  .slide-dots{position:absolute;left:20px;top:140px;display:flex;flex-direction:column;gap:6px}
  .slide-dots span{width:9px;height:9px;border-radius:50%;background:var(--white)}
  .slide-dots .on{background:var(--blue)}
  .mega-menu{position:absolute;left:700px;top:100px;width:400px;height:200px;background:var(--white);border-radius:0 0 8px 8px;box-shadow:0 4px 14px rgba(0,0,0,.18);display:flex;gap:22px;padding:14px 18px;font-size:9.5px;line-height:1.5}
  .mega-menu h4{font-size:10px;font-weight:700;letter-spacing:.3px;margin-bottom:2px}
  .mega-menu ul{list-style:none;margin-bottom:10px}
  .thumbs{display:flex;gap:6px;margin-bottom:8px}
  .thumb{width:46px;height:22px;background:linear-gradient(135deg,#7a8a94,#3e5566)}
  .article{font-size:8px;color:var(--gray);line-height:1.3;width:110px}
  .partner-band{position:absolute;left:60px;top:470px;width:1080px;height:80px;background:var(--blue);display:flex;align-items:center;justify-content:space-around;color:var(--white);font-size:17px;font-weight:600;letter-spacing:.5px}
  .section-head{position:absolute;left:100px;top:580px;width:1000px;display:flex;justify-content:space-between;align-items:center;font-size:12px;font-weight:700;letter-spacing:.5px}
  .arrows{display:flex;gap:16px}
</style>
</head>
<body>
  <header class="site-header">
    <div class="brand">tide-LOOP.</div>
    <div class="utility">
      <div class="search">Search for Products</div>
      <div class="filter-btn">Filter Products</div>
      <div class="social"><span></span><span></span><span></span><span></span><span></span></div>
      <div class="account">LOGIN<i>|</i>REGISTER</div>
    </div>
    <nav class="main-nav">
      <span>HOME</span><span class="active">EXPLORE</span><span>FORUMS</span><span>FEATURES</span><span>COLUMNS</span><span>DESTINATIONS</span><span>SHOP</span><span>LOCAL KNOWLEDGE</span>
    </nav>
  </header>

  <section class="hero" role="img" aria-label="Close-up of an angler's hand working a spinning reel on a rod">
    <div class="slide-dots"><span class="on"></span><span></span><span></span><span></span></div>
    <h1 class="hero-title">WELCOME<br>TO tide-LOOP.</h1>
  </section>

  <div class="mega-menu">
    <div>
      <h4>FISHING</h4>
      <ul><li>Offshore</li><li>Inshore</li><li>Fly Fishing</li><li>Freshwater</li><li>Gear</li><li>How-To</li><li>Fishin' Chicks</li><li>Hot Reports</li></ul>
    </div>
    <div>
      <h4>TRAVEL</h4>
      <ul><li>By Destination</li><li>TL Travel</li><li>Race to Ensenada</li><li>Fishing</li><li>Hunting</li><li>Weather</li></ul>
      <h4>RECIPIES</h4>
      <ul><li>Seafood</li><li>Wild Game</li></ul>
    </div>
    <div>
      <h4>BOATING</h4>
      <ul><li>Boats</li><li>Electronics</li><li>How-To</li><li>Safety</li><li>Gear</li><li>Engines</li><li>Classifieds</li><li>Charts</li></ul>
    </div>
    <div>
      <h4>FISHING VIDEOS</h4>
      <div class="thumbs"><div class="thumb" role="img" aria-label="Fishing video still"></div><div class="thumb" role="img" aria-label="Fishing video still"></div></div>
      <h4>FISH PHOTOS</h4>
      <div class="thumbs"><div class="thumb" role="img" aria-label="Catch photo"></div><div class="thumb" role="img" aria-label="Catch photo"></div></div>
      <h4>FISHING ARTICLES</h4>
      <p class="article">A Feast Of Billfish And More Over A Fall Weekend</p>
    </div>
  </div>

  <section class="partner-band">
    <span>Coastline Co.</span><span>Keelwear</span><span>Arcrod</span><span>Spoolmark</span><span>Baitline</span><span>Hookworks</span>
  </section>

  <div class="section-head">
    <span>LATEST UPDATES</span>
    <div class="arrows">
      <svg width="10" height="12" viewBox="0 0 10 12"><path d="M7 1 2 6l5 5" fill="none" stroke="#333333" stroke-width="2"/></svg>
      <svg width="10" height="12" viewBox="0 0 10 12"><path d="M3 1l5 5-5 5" fill="none" stroke="#333333" stroke-width="2"/></svg>
    </div>
  </div>
</body>
</html>
```